We need visit card and a letter paper for our website. thx

We have a beauty clinic in Switzerland.
https://wolkenbachtal.ch
We need a visit card.

Requirements
Must have
• see colors on website

```html
<!DOCTYPE html>
<html lang="de">
<head>
<meta charset="utf-8">
<title>Wolkenbachtal – Visitenkarte</title>
<link rel="stylesheet" href="https://fonts.googleapis.com/css2?family=Arimo:wght@400;700&display=swap">
<style>
  :root {
    --backdrop: #f2f2f2;
    --card-white: #ffffff;
    --card-black: #060609;
    --ink: #0d0d0d;
    --rose: #d5427c;
    --line-light: #ffffff;
    --hairline: #c9c9c9;
  }
  * { box-sizing: border-box; margin: 0; padding: 0; }
  html, body {
    width: 1200px; height: 616px; overflow: hidden;
    background: var(--backdrop);
    font-family: "Arimo", Arial, sans-serif;
  }
  .sheet {
    width: 1200px; height: 616px;
    display: flex; align-items: center; justify-content: center; gap: 40px;
  }
  .card {
    width: 540px; height: 337px; position: relative;
  }
  .card--front {
    background: var(--card-white);
    border: 1px solid var(--hairline);
    display: flex; align-items: center; justify-content: center;
  }
  .clinic-name {
    font-size: 50px; font-weight: 400; color: var(--ink); letter-spacing: 0.5px;
  }
  .card--back { background: var(--card-black); }
  .doctor {
    position: absolute; top: 72px; left: 0; right: 0; text-align: center;
    font-size: 17px; color: var(--rose); text-transform: uppercase;
  }
  .doctor__title { font-weight: 700; }
  .doctor__name { font-weight: 400; }
  .frame {
    position: absolute; left: 149px; top: 122px; width: 242px; height: 125px;
  }
  .contact {
    position: absolute; left: 0; right: 0; top: 160px;
    color: var(--line-light); font-size: 15px; text-align: center;
    display: flex; flex-direction: column; align-items: center; gap: 5px;
  }
  .contact__row { display: flex; align-items: center; gap: 12px; white-space: nowrap; }
  .contact__item { display: inline-flex; align-items: center; gap: 5px; }
  .icon { width: 15px; height: 15px; flex: none; }
</style>
</head>
<body>
<main class="sheet">
  <section class="card card--front" aria-label="Vorderseite">
    <h1 class="clinic-name">Wolkenbachtal</h1>
  </section>

  <section class="card card--back" aria-label="Rückseite">
    <p class="doctor"><span class="doctor__title">Dr. med. univ.</span> <span class="doctor__name">Lena Marbach</span></p>

    <svg class="frame" viewBox="0 0 242 125" aria-hidden="true">
      <g fill="none" stroke="#ffffff" stroke-width="2">
        <polyline points="1,34 1,1 241,1 241,34"/>
        <polyline points="1,94 1,124 241,124 241,94"/>
      </g>
    </svg>

    <address class="contact" style="font-style:normal">
      <div class="contact__row">
        <span class="contact__item">
          <svg class="icon" viewBox="0 0 16 16" aria-hidden="true"><circle cx="8" cy="8" r="8" fill="#d5427c"/><path d="M8 3.5a3 3 0 0 0-3 3c0 2.2 3 5.5 3 5.5s3-3.3 3-5.5a3 3 0 0 0-3-3z" fill="#fff"/><circle cx="8" cy="6.5" r="1.1" fill="#d5427c"/></svg>
          Bachweg 12, 7554 Sent, Switzerland
        </span>
      </div>
      <div class="contact__row">
        <span class="contact__item">
          <svg class="icon" viewBox="0 0 16 16" aria-hidden="true"><circle cx="8" cy="8" r="8" fill="#d5427c"/><path d="M5.3 4.2l1.4-.3.8 2-.9.7a5 5 0 0 0 2.8 2.8l.7-.9 2 .8-.3 1.4c-3.6.3-6.8-2.9-6.5-6.5z" fill="#fff"/></svg>
          +41 (0) 800 24 60 60
        </span>
        <span class="contact__item">
          <svg class="icon" viewBox="0 0 16 16" aria-hidden="true"><circle cx="8" cy="8" r="8" fill="#d5427c"/><rect x="4" y="5.2" width="8" height="5.6" rx="0.8" fill="#fff"/><polyline points="4.3,5.6 8,8.3 11.7,5.6" fill="none" stroke="#d5427c" stroke-width="0.9"/></svg>
          hallo@wolkenbachtal.ch
        </span>
      </div>
      <div class="contact__row">
        <span class="contact__item">
          <svg class="icon" viewBox="0 0 16 16" aria-hidden="true"><circle cx="8" cy="8" r="8" fill="#d5427c"/><g fill="none" stroke="#fff" stroke-width="1"><circle cx="8" cy="8" r="3.6"/><ellipse cx="8" cy="8" rx="1.5" ry="3.6"/><line x1="4.4" y1="8" x2="11.6" y2="8"/></g></svg>
          www.wolkenbachtal.ch
        </span>
      </div>
    </address>
  </section>
</main>
</body>
</html>
```